R&t subterra

We specialize in CIPP pipe lining but do other underground utilities trenchless as well.

Target Market(s)

Trenchless sewer replacement

Contact Information for Business Card

Doug Falvey 715-482-6170 Birchwood Falls, MN

```html
<!DOCTYPE html>
<html lang="en">
<head>
<meta charset="utf-8">
<title>R&amp;T Subterra – Business Card</title>
<link rel="stylesheet" href="https://fonts.googleapis.com/css2?family=Lato:wght@400;700;900&display=swap">
<style>
  :root {
    --backdrop: #1f1f1f;
    --brand-blue: #2b8bd0;
    --sky-edge: #7cc0e6;
    --sky-mid: #cfe7f5;
    --card-white: #ffffff;
    --ink: #2a2a2a;
  }
  * { box-sizing: border-box; margin: 0; padding: 0; }
  html, body {
    width: 1200px; height: 825px; overflow: hidden;
    background: var(--backdrop);
    font-family: "Lato", sans-serif;
  }
  .sheet {
    width: 1200px; height: 825px;
    display: flex; align-items: center; justify-content: center; gap: 40px;
  }
  .card {
    width: 540px; height: 308px;
    border-radius: 22px;
    position: relative;
    overflow: hidden;
  }
  .card--front {
    background: radial-gradient(ellipse 60% 60% at 50% 50%, #f6f7f8 0%, var(--sky-mid) 55%, var(--sky-edge) 100%);
    display: flex; align-items: center; justify-content: center;
  }
  .card--back {
    background: var(--card-white);
    display: flex; align-items: center; padding-left: 56px;
  }
  .brand {
    display: flex; align-items: center; gap: 12px;
  }
  .brand__dot {
    width: 44px; height: 44px; border-radius: 50%;
    background: var(--brand-blue);
    flex: none;
  }
  .brand__name {
    font-weight: 900;
    color: var(--brand-blue);
    font-size: 36px;
    letter-spacing: 0.5px;
    line-height: 1;
    text-transform: uppercase;
    white-space: nowrap;
  }
  .card--back .brand__dot { width: 30px; height: 30px; }
  .card--back .brand__name { font-size: 24px; }
  .divider {
    width: 2px; height: 110px;
    background: var(--brand-blue);
    margin: 0 24px 0 22px;
    flex: none;
  }
  .contact { white-space: nowrap; }
  .contact__name {
    font-weight: 900; color: var(--brand-blue);
    font-size: 24px; text-transform: uppercase; letter-spacing: 0.3px;
    margin-bottom: 8px;
  }
  .contact__line {
    display: flex; align-items: center; gap: 8px;
    font-size: 14px; color: var(--ink); margin-top: 5px;
  }
  .contact__line svg { width: 12px; height: 14px; flex: none; }
</style>
</head>
<body>
<main class="sheet">
  <section class="card card--front" aria-label="Card front">
    <div class="brand">
      <span class="brand__dot"></span>
      <span class="brand__name">R&amp;T Subterra</span>
    </div>
  </section>

  <section class="card card--back" aria-label="Card back">
    <div class="brand">
      <span class="brand__dot"></span>
      <span class="brand__name">R&amp;T Subterra</span>
    </div>
    <div class="divider"></div>
    <div class="contact">
      <p class="contact__name">Doug Falvey</p>
      <p class="contact__line">
        <svg viewBox="0 0 12 14" aria-hidden="true"><rect x="2" y="0.8" width="8" height="12.4" rx="1.5" fill="none" stroke="#2b8bd0" stroke-width="1.4"/><circle cx="6" cy="11" r="0.8" fill="#2b8bd0"/></svg>
        715-482-6170
      </p>
      <p class="contact__line">
        <svg viewBox="0 0 12 14" aria-hidden="true"><path d="M6 13.5C6 13.5 1 8.3 1 5.2A5 5 0 0 1 11 5.2C11 8.3 6 13.5 6 13.5Z" fill="#2b8bd0"/><circle cx="6" cy="5.2" r="1.8" fill="#fff"/></svg>
        Birchwood Falls, MN
      </p>
    </div>
  </section>
</main>
</body>
</html>
```